Sign Design

We already have a logo, but would like to design 2 x signs.
Sign 1:
Dimensions 1500mm wide x 2500m high.
Information to include on sign: - Clinic name and logo (attached)
- the word "DENTIST "
- Street number (which is 847)
Phone number (which is 6154 3970)

Sign 2:
Dimensions: 800mm wide x 600mm high

```html
<!DOCTYPE html>
<html lang="en">
<head>
<meta charset="utf-8">
<title>Ferncliff Dental Care – Sign Set</title>
<link rel="stylesheet" href="https://fonts.googleapis.com/css2?family=Bebas+Neue&family=Open+Sans:ital,wght@0,400;0,700;1,700&display=swap">
<style>
  :root {
    --forest: #066838;
    --leaf: #a5cf4f;
    --grass: #2db44a;
    --paper: #f4f9fd;
    --paper-edge: #e6f0f8;
    --ink-green: #0b7a3e;
    --white: #ffffff;
  }
  * { margin: 0; padding: 0; box-sizing: border-box; }
  html, body { width: 1200px; height: 2644px; overflow: hidden; }
  body { background: var(--forest); position: relative; font-family: "Open Sans", Arial, sans-serif; }

  .sign { position: absolute; overflow: hidden;
    background: radial-gradient(ellipse at 50% 35%, var(--white) 0%, var(--paper) 55%, var(--paper-edge) 100%); }
  .sign-tall { left: 210px; top: 189px; width: 786px; height: 1304px; }
  .sign-wide { left: 104px; top: 1629px; width: 1005px; height: 750px; }

  .wave { position: absolute; left: 0; top: 0; width: 100%; height: 100%; }
  .wave-dark { fill: var(--forest); }
  .wave-leaf { fill: var(--leaf); }
  .wave-grass { fill: var(--grass); }

  .brand { position: absolute; display: flex; align-items: center; }
  .brand-dot { border-radius: 50%; background: var(--leaf); flex: none; }
  .brand-name { color: var(--ink-green); font-weight: 400; line-height: 1.05; letter-spacing: -1px; }
  .brand-name span { display: block; }

  .sign-tall .brand { left: 125px; top: 110px; gap: 34px; }
  .sign-tall .brand-dot { width: 150px; height: 150px; }
  .sign-tall .brand-name .line-main { font-size: 72px; }
  .sign-tall .brand-name .line-sub { font-size: 42px; padding-left: 120px; }

  .title { position: absolute; font-family: "Bebas Neue", Impact, sans-serif; }
  .sign-tall .title { left: 0; right: 0; top: 338px; text-align: center; font-size: 116px; color: var(--leaf); letter-spacing: 2px; }

  .intro-head { position: absolute; font-weight: 700; font-style: italic; color: var(--forest); }
  .intro-body { position: absolute; color: #1d1d1d; }
  .sign-tall .intro-head { left: 0; right: 0; top: 470px; text-align: center; font-size: 30px; }
  .sign-tall .intro-body { left: 0; right: 0; top: 524px; text-align: center; font-size: 28px; line-height: 1.55; }

  .contact { position: absolute; color: var(--white); font-family: "Bebas Neue", Impact, sans-serif; display: flex; align-items: center; }
  .icon { fill: var(--white); flex: none; }

  .sign-tall .phone { left: 0; right: 0; top: 888px; justify-content: center; gap: 14px; font-size: 104px; letter-spacing: 3px; }
  .sign-tall .phone .icon { width: 78px; height: 78px; }
  .sign-tall .email { left: 0; right: 0; top: 1020px; justify-content: center; gap: 18px; font-size: 34px; letter-spacing: 2px; }
  .sign-tall .email .icon { width: 58px; height: 42px; fill: none; stroke: var(--white); stroke-width: 3; }
  .sign-tall .pin-mark { left: 0; right: 0; top: 1088px; justify-content: center; }
  .sign-tall .pin-mark .icon { width: 40px; height: 56px; }
  .sign-tall .street { left: 0; right: 0; top: 1160px; justify-content: center; font-size: 36px; letter-spacing: 2px; }

  .sign-wide .brand { left: 87px; top: 110px; gap: 48px; }
  .sign-wide .brand-dot { width: 230px; height: 230px; }
  .sign-wide .brand-name .line-main { font-size: 98px; }
  .sign-wide .brand-name .line-sub { font-size: 58px; padding-left: 180px; }

  .sign-wide .intro-head { right: 134px; top: 446px; text-align: right; font-size: 19px; color: var(--white); }
  .sign-wide .intro-body { right: 134px; top: 478px; text-align: right; font-size: 18px; line-height: 1.5; color: var(--white); }

  .sign-wide .phone { left: 0; top: 566px; width: 590px; justify-content: center; gap: 10px; font-size: 104px; letter-spacing: 3px; }
  .sign-wide .phone .icon { width: 78px; height: 78px; }
  .divider { position: absolute; left: 603px; top: 548px; width: 4px; height: 122px; background: var(--white); }
  .sign-wide .title { left: 634px; top: 552px; font-size: 64px; color: var(--white); letter-spacing: 16px; }
  .sign-wide .street { left: 636px; top: 630px; gap: 10px; font-size: 29px; letter-spacing: 1.5px; }
  .sign-wide .street .icon { width: 24px; height: 34px; }
</style>
</head>
<body>

  <section class="sign sign-tall">
    <svg class="wave" viewBox="0 0 370 614" preserveAspectRatio="none" aria-hidden="true">
      <path class="wave-dark" d="M0,352 C60,330 120,372 170,373 C230,374 255,308 300,304 C342,300 362,350 370,386 L370,614 L0,614 Z"/>
      <path class="wave-leaf" d="M0,402 C30,378 90,380 150,396 C210,412 250,346 300,338 C345,333 362,400 366,470 L366,614 L0,614 Z"/>
    </svg>

    <div class="brand">
      <div class="brand-dot"></div>
      <div class="brand-name"><span class="line-main">Ferncliff</span><span class="line-sub">Dental Care</span></div>
    </div>

    <h1 class="title">Dentist</h1>
    <p class="intro-head">What is Lorem Ipsum?</p>
    <p class="intro-body">Lorem Ipsum is simply dummy text of the<br>nting and typesetting industry.</p>

    <div class="contact phone">
      <svg class="icon" viewBox="0 0 24 24" aria-hidden="true"><path d="M6.6 10.8a15.2 15.2 0 0 0 6.6 6.6l2.2-2.2a1 1 0 0 1 1-.25 11.4 11.4 0 0 0 3.6.57 1 1 0 0 1 1 1V20a1 1 0 0 1-1 1A17 17 0 0 1 3 4a1 1 0 0 1 1-1h3.5a1 1 0 0 1 1 1c0 1.250.2 2.45.57 3.57a1 1 0 0 1-.25 1z"/></svg>
      <span>6154 3970</span>
    </div>
    <div class="contact email">
      <svg class="icon" viewBox="0 0 40 28" aria-hidden="true"><rect x="2" y="2" width="36" height="24"/><path d="M2 2 L20 16 L38 2 M2 26 L15 12 M38 26 L25 12"/></svg>
      <span>hello@ferncliffdental.com</span>
    </div>
    <div class="contact pin-mark">
      <svg class="icon" viewBox="0 0 24 34" aria-hidden="true"><path d="M12 0C5.4 0 0 5.3 0 11.8 0 20.6 12 34 12 34s12-13.4 12-22.2C24 5.3 18.6 0 12 0zm0 16.5a4.8 4.8 0 1 1 0-9.6 4.8 4.8 0 0 1 0 9.6z"/></svg>
    </div>
    <div class="contact street"><span>Street Number 847</span></div>
  </section>

  <section class="sign sign-wide">
    <svg class="wave" viewBox="0 0 473 353" preserveAspectRatio="none" aria-hidden="true">
      <path class="wave-dark" d="M0,208 C80,188 150,196 220,186 C290,176 340,150 395,158 C440,166 465,198 473,218 L473,353 L0,353 Z"/>
      <path class="wave-grass" d="M0,234 C80,222 200,224 280,206 C330,194 360,172 405,174 C442,176 462,204 468,230 L468,353 L0,353 Z"/>
    </svg>

    <div class="brand">
      <div class="brand-dot"></div>
      <div class="brand-name"><span class="line-main">Ferncliff</span><span class="line-sub">Dental Care</span></div>
    </div>

    <p class="intro-head">What is Lorem Ipsum?</p>
    <p class="intro-body">Lorem Ipsum is simply dummy text of<br>the nting and typesetting industry.</p>

    <div class="contact phone">
      <svg class="icon" viewBox="0 0 24 24" aria-hidden="true"><path d="M6.6 10.8a15.2 15.2 0 0 0 6.6 6.6l2.2-2.2a1 1 0 0 1 1-.25 11.4 11.4 0 0 0 3.6.57 1 1 0 0 1 1 1V20a1 1 0 0 1-1 1A17 17 0 0 1 3 4a1 1 0 0 1 1-1h3.5a1 1 0 0 1 1 1c0 1.25.2 2.45.57 3.57a1 1 0 0 1-.25 1z"/></svg>
      <span>6154 3970</span>
    </div>
    <div class="divider"></div>
    <h2 class="title">Dentist</h2>
    <div class="contact street">
      <svg class="icon" viewBox="0 0 24 34" aria-hidden="true"><path d="M12 0C5.4 0 0 5.3 0 11.8 0 20.6 12 34 12 34s12-13.4 12-22.2C24 5.3 18.6 0 12 0zm0 16.5a4.8 4.8 0 1 1 0-9.6 4.8 4.8 0 0 1 0 9.6z"/></svg>
      <span>Street Number 847</span>
    </div>
  </section>

</body>
</html>
```